Business cards for Harbourline Supply Pty Ltd that import building products into Australia from China
Target Market(s)
Business to Business
Industry/Entity Type
Business
Contact Information for Business Card
Front: Logo and Business Name
Rear:
Vernon Ashcombe
General Manager
Mobile: 0427 619 354
email: vern@harbourlinesupply.com.au
alternative email: vern@coastwardgoods.com.au
web: www.harbourlinesupply.com.au
Adelaide, Brisbane and Darwin
Colors
ec1f27
fbee3d

```html
<!DOCTYPE html>
<html lang="en">
<head>
<meta charset="utf-8">
<title>Harbourline Supply – Business Cards</title>
<link rel="stylesheet" href="https://fonts.googleapis.com/css2?family=Josefin+Sans:wght@400;600;700&display=swap">
<style>
  :root {
    --brand-red: #e42229;
    --paper: #f2f1ef;
    --ink: #3b3b3d;
    --backdrop: #c9ced6;
    --backdrop-light: #e4e7ec;
    --white: #ffffff;
  }
  * { box-sizing: border-box; margin: 0; padding: 0; }
  html, body { width: 1200px; height: 1000px; overflow: hidden; }
  body {
    background: linear-gradient(160deg, var(--backdrop-light) 0%, var(--backdrop) 100%);
    font-family: "Josefin Sans", sans-serif;
    position: relative;
  }
  .card {
    position: absolute;
    width: 560px;
    height: 340px;
    box-shadow: 0 14px 30px rgba(40, 45, 60, 0.22);
    overflow: hidden;
  }
  /* Front card */
  .card--front {
    left: 560px;
    top: 90px;
    background: var(--brand-red);
  }
  .frame { position: absolute; border-color: var(--white); border-style: solid; }
  .card--front .frame--top {
    right: 0; top: 0;
    width: 300px; height: 150px;
    border-width: 16px 22px 0 0;
  }
  .card--front .frame--bottom {
    right: 0; bottom: 0;
    width: 70px; height: 110px;
    border-width: 0 22px 16px 0;
  }
  .front-name {
    position: absolute;
    left: 80px;
    top: 120px;
    display: flex;
    align-items: center;
    gap: 16px;
    color: var(--white);
    font-weight: 700;
    font-size: 34px;
    line-height: 1.05;
    letter-spacing: 0.5px;
    text-transform: uppercase;
  }
  .front-name .mark {
    width: 22px; height: 22px;
    background: var(--white);
    flex: none;
  }
  .front-web {
    position: absolute;
    left: 118px;
    top: 262px;
    color: var(--white);
    font-size: 15px;
    letter-spacing: 2px;
    text-transform: uppercase;
  }
  /* Back card */
  .card--back {
    left: 110px;
    top: 500px;
    background: var(--paper);
  }
  .card--back .frame { border-color: var(--brand-red); }
  .card--back .frame--top {
    left: 0; top: 0;
    width: 70px; height: 120px;
    border-width: 16px 0 0 22px;
  }
  .card--back .frame--bottom {
    left: 0; bottom: 0;
    width: 260px; height: 140px;
    border-width: 0 0 16px 22px;
  }
  .contact {
    position: absolute;
    left: 120px;
    top: 80px;
    color: var(--ink);
    text-transform: uppercase;
    letter-spacing: 1px;
  }
  .person-name { color: var(--brand-red); font-size: 19px; font-weight: 600; }
  .person-title { font-size: 17px; margin-top: 4px; }
  .details { margin-top: 34px; font-size: 15px; line-height: 1.45; list-style: none; }
  .details .label { color: var(--brand-red); font-weight: 600; display: inline-block; width: 16px; }
  .details .indent { padding-left: 0; }
  /* Logo tile */
  .logo-tile {
    position: absolute;
    right: 40px;
    bottom: 30px;
    width: 170px;
    height: 150px;
    background: var(--white);
    display: flex;
    align-items: center;
    justify-content: center;
    gap: 10px;
    padding: 12px;
  }
  .logo-tile .mark { width: 14px; height: 14px; background: #111; flex: none; }
  .logo-tile .tile-name {
    color: #111;
    font-weight: 700;
    font-size: 19px;
    line-height: 1.05;
    text-transform: uppercase;
  }
</style>
</head>
<body>
  <section class="card card--front" aria-label="Card front">
    <div class="frame frame--top"></div>
    <div class="frame frame--bottom"></div>
    <div class="front-name"><span class="mark"></span><span>Harbourline<br>Supply Pty Ltd</span></div>
    <p class="front-web">www.harbourlinesupply.com.au</p>
  </section>

  <section class="card card--back" aria-label="Card back">
    <div class="frame frame--top"></div>
    <div class="frame frame--bottom"></div>
    <div class="contact">
      <p class="person-name">Vernon Ashcombe</p>
      <p class="person-title">General Manager</p>
      <ul class="details">
        <li><span class="label">M</span> 0427 619 354</li>
        <li><span class="label">E</span> vern@harbourlinesupply.com.au</li>
        <li class="indent">or vern@coastwardgoods.com.au</li>
      </ul>
    </div>
  </section>

  <div class="logo-tile">
    <span class="mark"></span>
    <span class="tile-name">Harbourline<br>Supply Pty Ltd</span>
  </div>
</body>
</html>
```